Moder Business Card Design for Renewables Business

Need a business card design for my business. We collect & repurpose spent coffee ground from cafes. The cards will be made from recycled paper. Needs to fit our corporate colour scheme of white, green & brown (see logo for colour codes). Eco friendly, modern, intresting & eye catching.
This card needs to convey the message of the business and fit into its mantra of eco-friendly, sustainable etc.

Target Market(s)

Cafe Owners, Coffee Drinkers, Recycling Companies, Farmers

Industry/Entity Type

Recycling

Contact Information for Business Card

Name; Peter Halloran
Phone; 0412 386 527
e-mail; info@lumatrove.com.au
website; www.lumatrove.com.au

Font styles to use
Sans Serif
Script

Colors

Designer to choose colors to be used in the design.

Requirements
Must have
• FRONT;
• Logo, Name (Peter Halloran), phone number, e-mail address, website
• BACK;
• On the back in cursive text; 'GOOD THINGS FROM EVERY LAST CUP'
• Small facebook & Instagram logos with text 'Lumatrove'
Should not have
• messy design

```html
<!DOCTYPE html>
<html lang="en">
<head>
<meta charset="utf-8">
<title>Lumatrove Business Card</title>
<link href="https://fonts.googleapis.com/css2?family=Arimo:wght@400;700&family=Lobster+Two:ital,wght@1,700&display=swap" rel="stylesheet">
<style>
  :root {
    --backdrop: #b4b4b4;
    --card: #f7f7f5;
    --green: #6b9a2f;
    --brown: #5b3a1d;
    --ink: #3a3a3a;
    --emboss: #e2e2df;
  }
  * { box-sizing: border-box; margin: 0; padding: 0; }
  html, body { width: 1200px; height: 814px; overflow: hidden; }
  body {
    background: var(--backdrop);
    font-family: "Arimo", Arial, sans-serif;
    position: relative;
  }
  .card {
    position: absolute;
    top: 257px;
    width: 525px;
    height: 300px;
    background: var(--card);
    box-shadow: 0 6px 18px rgba(0,0,0,.18);
  }
  .card--back { left: 40px; }
  .card--front { left: 635px; }

  /* back side */
  .brand {
    position: absolute;
    left: 0; right: 0; top: 62px;
    text-align: center;
  }
  .brand__dot {
    display: block;
    width: 74px; height: 74px;
    margin: 0 auto 8px;
    border: 6px solid var(--green);
    border-radius: 50%;
  }
  .brand__name {
    font-size: 30px;
    font-weight: 700;
    letter-spacing: 1px;
    color: var(--green);
  }
  .tagline {
    position: absolute;
    left: 0; right: 0; top: 196px;
    text-align: center;
    font-family: "Lobster Two", cursive;
    font-style: italic;
    font-weight: 700;
    font-size: 30px;
    color: var(--brown);
  }
  .social {
    position: absolute;
    top: 22px; right: 24px;
    display: flex; align-items: center; gap: 6px;
    font-size: 12px;
    color: var(--green);
  }
  .social__dot {
    width: 11px; height: 11px;
    border-radius: 50%;
    background: var(--green);
  }

  /* front side */
  .emboss-mark {
    position: absolute;
    left: 62px; top: 40px;
    width: 96px; height: 96px;
    border: 3px solid var(--emboss);
    border-radius: 50%;
    box-shadow: 1px 1px 0 #fff inset, -1px -1px 0 #d4d4d0 inset;
  }
  .contact {
    position: absolute;
    left: 250px; right: 22px; top: 48px;
    color: var(--ink);
  }
  .contact__rule { height: 2px; background: var(--brown); opacity: .7; }
  .contact__name {
    font-size: 17px;
    font-weight: 700;
    letter-spacing: 1px;
    color: var(--green);
    text-transform: uppercase;
    padding: 8px 0 8px 24px;
  }
  .contact__phone { font-size: 22px; letter-spacing: 1px; margin-top: 8px; }
  .contact__line { font-size: 14px; margin-top: 3px; }
</style>
</head>
<body>
  <section class="card card--back" aria-label="Card back">
    <div class="social"><span class="social__dot"></span>Lumatrove</div>
    <div class="brand">
      <span class="brand__dot"></span>
      <div class="brand__name">LUMATROVE</div>
    </div>
    <p class="tagline">Good things from every last cup</p>
  </section>

  <section class="card card--front" aria-label="Card front">
    <div class="emboss-mark"></div>
    <div class="contact">
      <div class="contact__rule"></div>
      <div class="contact__name">Peter Halloran</div>
      <div class="contact__rule"></div>
      <div class="contact__phone">0412 386 527</div>
      <div class="contact__line">info@lumatrove.com.au</div>
      <div class="contact__line">www.lumatrove.com.au</div>
    </div>
  </section>
</body>
</html>
```